Certified Notary Signing Agent Business Card Design

I need a modern, visually appealing two-sided business card for my mobile notary signing agent business which clearly communicates my certification by the Federal Signatory Guild ("FSG") and Deed Closing Method ("DCM"). It should be clean and easy to read and trust focused. While I am not committed to specific fonts and colors, I do like the colors in both my final logo and a sample logo (color examples only). I want to hand out a business card that is easy to locate in a stack and differentiates itself easily from others as it is an extremely crowded market space.

Target Market(s)

Title Companies, Escrow Officers, Real Estate Agents, Real Estate Lenders

Industry/Entity Type

Real Estate Lending

Contact Information for Business Card

I need a two-sided business card for my mobile notary signing agent business that prominently displays my photo, logo (potentially, just on the back), my service areas, phone, email, url and an FSG certification and DCM certification. On the back side of the card I would like my url, logo and potentially certification icons. On the back, I MAY want to add language that I have been an FSG Certified NSA for 10 + years and have performed over 8k in real estate loan transactions. I have attached a very old biz card circa 2007 that I designed myself on a card ordering platform. While it's not great, it can display how I crammed all of the data on a single card. I am NOT suggesting replicating this design in any form but provide it as reference material only,

Font styles to use
Sans Serif

Requirements
Must have
• Name: Mara Oltvany, Certified Notary Signing Agent Phone: 936.482.1795 URL: www.TopTierSealers.example Email: mara@toptiersealers.example, Counties serviced: Montgomery, Grimes, N. Harris, Walker, Waller, Federal Signatory Guild Badge, Deed Closing Method Badge (still need to upload this)
Nice to have
• I am open to color variations on my logo as illustrated in the attachment labeled as Logo Sample Colors Only (11A) that has a slate blue/grey background w/white lettering and gold pen and circles

```html
<!DOCTYPE html>
<html lang="en">
<head>
<meta charset="utf-8">
<title>Mara Oltvany – Business Card</title>
<link href="https://fonts.googleapis.com/css2?family=Arimo:wght@400;700&family=Poppins:wght@400;500&display=swap" rel="stylesheet">
<style>
  :root {
    --backdrop: #3e3e3e;
    --card-white: #ffffff;
    --slate: #37414c;
    --navy: #0d3585;
    --ink-grey: #555a60;
    --accent-red: #e23a3f;
    --gold: #c9b98a;
    --photo-light: #e9c1a8;
    --photo-mid: #c99474;
    --photo-hair: #b88955;
  }
  * { box-sizing: border-box; margin: 0; padding: 0; }
  html, body { width: 1200px; height: 1200px; overflow: hidden; }
  body { background: var(--backdrop); position: relative; font-family: "Arimo", Arial, sans-serif; }

  .card { position: absolute; width: 688px; height: 393px; border-radius: 22px; overflow: hidden; }

  /* Front */
  .card-front { left: 267px; top: 158px; background: var(--card-white); }
  .portrait {
    position: absolute; left: 0; top: 0; width: 314px; height: 100%;
    background: radial-gradient(ellipse at 45% 45%, var(--photo-light) 0%, var(--photo-mid) 60%, var(--photo-hair) 100%);
  }
  .identity { position: absolute; left: 357px; top: 66px; }
  .name { font-weight: 700; font-size: 26px; color: var(--navy); letter-spacing: 0.2px; }
  .title { font-size: 15px; color: var(--ink-grey); margin-top: 3px; }
  .rule { width: 21px; height: 1.5px; background: var(--navy); margin-top: 13px; }
  .contacts { list-style: none; margin-top: 25px; }
  .contacts li { display: flex; align-items: center; font-size: 16.5px; color: var(--ink-grey); height: 20.5px; }
  .contacts svg { width: 14px; height: 14px; margin-right: 11px; flex: none; }

  .badges { position: absolute; left: 353px; top: 278px; display: flex; align-items: center; gap: 16px; }
  .brand-mark { display: flex; align-items: center; gap: 6px; }
  .brand-dot { width: 14px; height: 14px; border-radius: 50%; border: 1.5px solid #222; }
  .brand-name { font-family: "Arimo", Arial, sans-serif; font-weight: 700; font-size: 12px; color: var(--navy); width: 70px; line-height: 1.2; }
  .cert-badge { width: 82px; height: 82px; border-radius: 50%; background: var(--accent-red); border: 8px solid #fbe3e4; }

  /* Back */
  .card-back { left: 262px; top: 652px; background: var(--slate); font-family: "Poppins", Arial, sans-serif; }
  .back-brand { position: absolute; left: 0; right: 0; top: 152px; display: flex; justify-content: center; align-items: center; gap: 14px; }
  .back-brand-dot { width: 22px; height: 22px; border-radius: 50%; border: 3px solid var(--gold); }
  .back-brand-name { font-weight: 500; font-size: 34px; color: #ffffff; letter-spacing: 1px; }
  .service-lines { position: absolute; left: 0; right: 0; top: 313px; text-align: center; color: #ffffff; font-size: 17px; line-height: 21px; }
  .sep { display: inline-block; width: 6px; height: 6px; border-radius: 50%; background: var(--gold); vertical-align: middle; margin: 0 14px; }
</style>
</head>
<body>
  <section class="card card-front">
    <div class="portrait" role="img" aria-label="Portrait photo of Mara Oltvany"></div>
    <div class="identity">
      <h1 class="name">MARA OLTVANY</h1>
      <p class="title">Certified Notary Signing Agent</p>
      <div class="rule"></div>
      <ul class="contacts">
        <li>
          <svg viewBox="0 0 24 24"><path fill="var(--accent-red)" d="M6.6 10.8a15 15 0 0 0 6.6 6.6l2.2-2.2c.3-.3.7-.4 1-.2 1.1.4 2.3.6 3.6.6.6 0 1 .4 1 1V20c0 .6-.4 1-1 1A17 17 0 0 1 3 4c0-.6.4-1 1-1h3.5c.6 0 1 .4 1 1 0 1.3.2 2.5.6 3.6.1.3 0 .7-.2 1z"/></svg>
          936.482.1795
        </li>
        <li>
          <svg viewBox="0 0 24 24"><rect x="2" y="5" width="20" height="14" fill="var(--accent-red)"/><path d="M2 5l10 8 10-8" fill="none" stroke="#fff" stroke-width="2"/></svg>
          mara@toptiersealers.example
        </li>
        <li>
          <svg viewBox="0 0 24 24"><circle cx="12" cy="12" r="10" fill="var(--accent-red)"/><path d="M8 7c2 1 3 3 2 5s-2 3-1 6M14 5c0 2 2 3 4 3" fill="none" stroke="#fff" stroke-width="1.6"/></svg>
          www.TopTierSealers.example
        </li>
      </ul>
    </div>
    <div class="badges">
      <div class="brand-mark">
        <span class="brand-dot"></span>
        <span class="brand-name">Top Tier Sealers</span>
      </div>
      <div class="cert-badge" role="img" aria-label="Federal Signatory Guild certification badge"></div>
    </div>
  </section>

  <section class="card card-back">
    <div class="back-brand">
      <span class="back-brand-dot"></span>
      <span class="back-brand-name">TOP TIER SEALERS</span>
    </div>
    <div class="service-lines">
      <p>Montgomery<span class="sep"></span>Grimes, N. Harris<span class="sep"></span>Walker<span class="sep"></span>Waller</p>
      <p>Federal Signatory Guild Badge<span class="sep"></span>Deed Closing Method Badge</p>
    </div>
  </section>
</body>
</html>
```